ご提案有難うございました。
最もサイトのトンマナにあっており、かつキャンペーンの売りが目立っていると感じたため、こちらのデザインを採用させて頂きました。
どれも素晴らしいご提案で御座いました。
また機会があればどうぞ宜しくお願い致します。
居酒屋予約 バナーデザイン バナー作成の仕事の依頼
希望する色 特になし・その他
バナーサイズ
• 300x250
目的・概要
居酒屋の割引キャンペーンページに誘導するために使用するバナー制作です。
依頼詳細
以下のページ等に設置致します。
https://www.quorvelia.com/asia/japan/japa-japan/japa-restaurant/shinjuku-izakaya/
▽入れてほしい画像▽
会社ロゴ
▽入れてほしい文言▽
※以下の文章例を参考に、バナーデザインに映えるようご調整ください
■文章例
【最大100%割引】税込み2,160円以上の飲食で2,000円のキャッシュバックキャンペーン中!
【最大100%割引】居酒屋利用で2,000円のキャッシュバックキャンペーン中!
【最大100%割引】2,160円(税込)以上の居酒屋利用で2,000円の現金還元中!
Quorvelia限定!居酒屋の利用で現金2,000円が貰える!
【最大100%割引】税込み2,160円の居酒屋利用で2,000円現金還元中!
Quorvelia限定企画!税込み2,160円の居酒屋利用で2,000円現金還元中!!
3000店舗以上から選べる!税込み2,160円の居酒屋利用で2,000円現金還元中!!
居酒屋代金、実質最大100%オフ
3000店以上の居酒屋が実質最大100%割引
居酒屋の利用で漏れなく現金2,000円が貰える
▽バナーサイズ▽
▽納品形式▽
png/jpg
▽注意点・禁止事項▽
※他のクライアントへ既に提案した内容の転用など
※作成いただいたバナーに関して、納品後はクライアントに帰属します。
たくさんのウェブデザイナーの方からのご提案をお待ちしております!

```html
<!DOCTYPE html>
<html lang="ja">
<head>
<meta charset="utf-8">
<title>居酒屋キャンペーン バナー案</title>
<link rel="stylesheet" href="https://fonts.googleapis.com/css2?family=M+PLUS+Rounded+1c:wght@700;800;900&display=swap">
<style>
  :root {
    --canvas: #ffffff;
    --frame: #3a3a3a;
    --night-deep: #0e2a66;
    --night-mid: #1f56b0;
    --night-glow: #3f86d8;
    --sunset-deep: #e0561c;
    --sunset-mid: #f28a2a;
    --sunset-glow: #fcc463;
    --headline-fill: #ffd23a;
    --headline-edge: #2a1d0c;
    --logo-blue: #1f6fd0;
    --cta-blue: #1e8fe6;
    --cta-text: #ffffff;
    --skyline: #1a1f3d;
    --people: #f3e7c8;
    --beer: #f0b43a;
    --food: #7a5a3a;
    --money: #c98a2c;
  }
  * { margin: 0; padding: 0; box-sizing: border-box; }
  html, body { width: 1200px; height: 708px; overflow: hidden; background: var(--canvas); }
  body { position: relative; font-family: "M PLUS Rounded 1c", sans-serif; }

  .banner {
    position: absolute;
    top: 186px;
    width: 460px;
    height: 362px;
    overflow: hidden;
    border: 2px solid var(--frame);
  }
  .banner--night { left: 110px; background: radial-gradient(circle at 50% 40%, var(--night-glow) 0%, var(--night-mid) 45%, var(--night-deep) 100%); }
  .banner--sunset { left: 640px; background: radial-gradient(circle at 55% 45%, var(--sunset-glow) 0%, var(--sunset-mid) 45%, var(--sunset-deep) 100%); }

  .brand {
    position: absolute; top: 12px; left: 14px;
    display: flex; align-items: center; gap: 6px;
    background: #ffffff; padding: 3px 8px; border-radius: 4px;
    z-index: 3;
  }
  .brand__mark { width: 12px; height: 12px; background: var(--logo-blue); }
  .brand__name { font-size: 15px; font-weight: 800; color: var(--logo-blue); }

  .art { position: absolute; z-index: 1; }
  .art--food { top: 10px; left: 250px; width: 80px; height: 34px; border-radius: 8px; background: var(--food); opacity: .85; }
  .art--beer { top: 10px; left: 345px; width: 70px; height: 78px; border-radius: 10px; background: var(--beer); }
  .art--people { bottom: 0; left: 10px; width: 140px; height: 140px; border-radius: 60px 60px 0 0; background: var(--people); opacity: .92; }
  .art--skyline { bottom: 0; left: 150px; right: 0; height: 48px; background: var(--skyline); }
  .art--money { bottom: 60px; left: 180px; width: 130px; height: 36px; border-radius: 18px; background: var(--money); opacity: .7; }

  .headline {
    position: absolute; z-index: 2;
    left: 18px; top: 82px; width: 420px;
    font-weight: 900;
    color: var(--headline-fill);
    -webkit-text-stroke: 2px var(--headline-edge);
    paint-order: stroke fill;
    text-shadow: 3px 3px 0 var(--headline-edge);
    line-height: 1.02;
    transform: rotate(-4deg);
  }
  .headline__amount { display: block; font-size: 56px; letter-spacing: -1px; }
  .headline__amount small { font-size: 28px; }
  .headline__free { display: block; font-size: 50px; padding-left: 14px; }
  .headline__eat { display: block; font-size: 50px; padding-left: 130px; }

  .cta {
    position: absolute; z-index: 3;
    right: 40px; bottom: 30px;
    padding: 7px 20px;
    background: var(--cta-blue);
    color: var(--cta-text);
    font-size: 16px; font-weight: 800;
    border-radius: 20px;
    border: 2px solid #ffffff;
  }
  .cta-arrow { position: absolute; z-index: 3; right: 16px; bottom: 20px; }
</style>
</head>
<body>

  <section class="banner banner--night" aria-label="居酒屋キャンペーン バナー 夜空版">
    <div class="brand"><span class="brand__mark"></span><span class="brand__name">Quorvelia</span></div>
    <div class="art art--food" role="img" aria-label="焼き鳥の串のイラスト"></div>
    <div class="art art--beer" role="img" aria-label="ビールジョッキのイラスト"></div>
    <div class="art art--skyline" role="img" aria-label="夜の街並みのシルエット"></div>
    <div class="art art--people" role="img" aria-label="乾杯する二人の会社員のイラスト"></div>
    <h2 class="headline">
      <span class="headline__amount">2000<small>円分</small></span>
      <span class="headline__free">タダで飲める!?</span>
      <span class="headline__eat">食べれる!?</span>
    </h2>
    <span class="cta">詳しくはこちら</span>
    <svg class="cta-arrow" width="18" height="18" viewBox="0 0 18 18" aria-hidden="true"><path d="M4 3l10 6-10 6z" fill="#ffffff"/></svg>
  </section>

  <section class="banner banner--sunset" aria-label="居酒屋キャンペーン バナー 夕焼け版">
    <div class="brand"><span class="brand__mark"></span><span class="brand__name">Quorvelia</span></div>
    <div class="art art--beer" role="img" aria-label="ビールジョッキのイラスト"></div>
    <div class="art art--money" role="img" aria-label="舞い散るお札と硬貨のイラスト"></div>
    <div class="art art--people" role="img" aria-label="乾杯する二人の会社員のイラスト"></div>
    <h2 class="headline">
      <span class="headline__amount">2000<small>円分</small></span>
      <span class="headline__free">タダで飲める!?</span>
      <span class="headline__eat">食べれる!?</span>
    </h2>
    <span class="cta">詳しくはこちら</span>
    <svg class="cta-arrow" width="18" height="18" viewBox="0 0 18 18" aria-hidden="true"><path d="M4 3l10 6-10 6z" fill="#ffffff"/></svg>
  </section>

</body>
</html>
```